Stationery Set for Brelvo Company

I need to create full stationery design for my company; Business Cards, Envelops, Letter Heads, Calendar.
In the letter head and Envelops... only contact information and website links.
Our company is a Service Management company with different domains of innovative services including Technology Service Management, Education Services, Outsourcing Management, Events Management.
I need a modern and innovative design specially for the business card. I some transparent designs and I like it, but don't limit your innovation to what I mentioned. Sky is limit for your innovation.

Target Market(s)

Middle East & Africa

Industry/Entity Type

Business Management

Colors
34a7d8
0355a3
85acd3
86cae7
cee9f5
cfdeed
e4daeb
f3f1f8
ecf7fb

Requirements
Must have
• Name, Title, Email, Mobile
Nice to have
• We have multiple locations in USA, KSA, EGY, so I need ideas about how to include all contact details maybe QR / Barcode or something else.
• Please see our locations and contact information: www.gofarnix.example
Should not have
• Too much text

```html
<!DOCTYPE html>
<html lang="en">
<head>
<meta charset="utf-8">
<title>Brelvo Company Stationery Set</title>
<link rel="stylesheet" href="https://fonts.googleapis.com/css2?family=Figtree:wght@400;600&display=swap">
<style>
:root{
  --backdrop:#c4c4c4;
  --paper:#ffffff;
  --brand-blue:#3b67b0;
  --deep-blue:#0d5fa8;
  --text-blue:#2957a4;
  --stone:#c9c0bd;
  --ink:#1e1e1e;
}
*{margin:0;padding:0;box-sizing:border-box}
html,body{width:1200px;height:1000px;overflow:hidden}
body{background:var(--backdrop);font-family:"Figtree",Arial,sans-serif;position:relative;color:var(--ink)}
.sheet{position:absolute;background:var(--paper);box-shadow:1px 2px 3px rgba(0,0,0,.35);overflow:hidden}
.sheet--blue{background:var(--brand-blue)}
.band{position:absolute;left:0;bottom:0;width:100%;display:block}
.brand{position:absolute;display:flex;align-items:center;gap:8px;font-weight:600;color:var(--brand-blue);white-space:nowrap}
.brand__dot{border-radius:50%;background:var(--stone);flex:none}
.brand--light{color:#fff}
.brand--light .brand__dot{background:var(--stone)}
.person{position:absolute}
.person__name{font-size:13px;font-weight:600;color:var(--text-blue)}
.person__title{font-size:8px;margin-top:2px}
.divider{position:absolute;width:1px;background:var(--brand-blue)}
.contacts{position:absolute;font-size:9.5px;line-height:12.5px}
.contacts__row{display:flex;align-items:center;gap:5px}
.contacts__gap{height:7px}
.contacts__addr{margin-top:8px}
.contacts__addr--blue{color:var(--text-blue)}
.icon{width:7px;height:7px;fill:var(--brand-blue);flex:none}
.mini{position:absolute;font-size:5px;line-height:6.5px}
.accent-disc{position:absolute;border-radius:50%;background:var(--brand-blue)}
.flap{position:absolute;left:0;top:0;width:100%}
</style>
</head>
<body>

<!-- Business card front, white -->
<section class="sheet" style="left:58px;top:24px;width:319px;height:197px">
  <div class="brand" style="left:62px;top:78px;font-size:22px"><span class="brand__dot" style="width:12px;height:12px"></span>Brelvo Company</div>
  <svg class="band" viewBox="0 0 319 20" height="20" preserveAspectRatio="none"><polygon points="0,0 212,0 207,20 0,20" fill="var(--stone)"/><polygon points="216,0 319,0 319,20 211,20" fill="var(--deep-blue)"/></svg>
</section>

<!-- Business card back, divided -->
<section class="sheet" style="left:446px;top:24px;width:319px;height:197px">
  <div class="person" style="left:41px;top:36px;text-align:right;width:100px">
    <div class="person__name">Lena Marsh</div><div class="person__title">Director</div>
  </div>
  <div class="brand" style="left:32px;top:114px;font-size:11px;gap:4px"><span class="brand__dot" style="width:6px;height:6px"></span>Brelvo Company</div>
  <div class="divider" style="left:160px;top:12px;height:148px"></div>
  <div class="contacts" style="left:172px;top:72px">
    <div class="contacts__row"><svg class="icon" viewBox="0 0 8 8"><rect x="2" y="0" width="4" height="8" rx="1"/></svg>+000 555 0147</div>
    <div class="contacts__row"><svg class="icon" viewBox="0 0 8 8"><rect x="0" y="3" width="8" height="5" rx="1"/><rect x="1" y="0" width="6" height="2" rx="1"/></svg>+000 555 0147</div>
    <div class="contacts__gap"></div>
    <div class="contacts__row"><svg class="icon" viewBox="0 0 8 8"><rect x="0" y="1" width="8" height="6" rx="1"/></svg>info@tarnwell.example</div>
    <div class="contacts__row"><svg class="icon" viewBox="0 0 8 8"><circle cx="4" cy="4" r="4"/></svg>www.tarnwell.example</div>
    <div class="contacts__addr">24 Orchard Lane, Redvale<br>City Name, Australia 9000</div>
  </div>
  <svg class="band" viewBox="0 0 319 20" height="20" preserveAspectRatio="none"><polygon points="0,0 212,0 207,20 0,20" fill="var(--stone)"/><polygon points="216,0 319,0 319,20 211,20" fill="var(--deep-blue)"/></svg>
</section>

<!-- Business card front, blue -->
<section class="sheet sheet--blue" style="left:848px;top:24px;width:318px;height:197px">
  <div class="brand brand--light" style="left:56px;top:78px;font-size:24px"><span class="brand__dot" style="width:12px;height:12px"></span>Brelvo Company</div>
</section>

<!-- Business card back, accent edge -->
<section class="sheet" style="left:46px;top:260px;width:319px;height:196px">
  <div class="accent-disc" style="left:-30px;top:150px;width:62px;height:62px"></div>
  <div class="person" style="left:118px;top:33px">
    <div class="person__name">Lena Marsh</div><div class="person__title">Director</div>
  </div>
  <div class="contacts" style="left:117px;top:81px">
    <div class="contacts__row"><svg class="icon" viewBox="0 0 8 8"><rect x="2" y="0" width="4" height="8" rx="1"/></svg>+000 555 0147</div>
    <div class="contacts__row"><svg class="icon" viewBox="0 0 8 8"><rect x="0" y="3" width="8" height="5" rx="1"/><rect x="1" y="0" width="6" height="2" rx="1"/></svg>+000 555 0147</div>
    <div class="contacts__gap"></div>
    <div class="contacts__row"><svg class="icon" viewBox="0 0 8 8"><rect x="0" y="1" width="8" height="6" rx="1"/></svg>info@mailbox.example</div>
    <div class="contacts__row"><svg class="icon" viewBox="0 0 8 8"><circle cx="4" cy="4" r="4"/></svg>www.sitename.example</div>
    <div class="contacts__addr contacts__addr--blue">24 Orchard Lane, Redvale<br>City Name, Country 9000</div>
  </div>
</section>

<!-- Business card back, divided, no bands -->
<section class="sheet" style="left:446px;top:260px;width:319px;height:196px">
  <div class="brand" style="left:20px;top:120px;font-size:11px;gap:4px"><span class="brand__dot" style="width:6px;height:6px"></span>Brelvo Company</div>
  <div class="divider" style="left:160px;top:24px;height:146px"></div>
  <div class="person" style="left:175px;top:27px">
    <div class="person__name">Lena Marsh</div><div class="person__title">Director</div>
  </div>
  <div class="contacts" style="left:174px;top:82px">
    <div class="contacts__row"><svg class="icon" viewBox="0 0 8 8"><rect x="2" y="0" width="4" height="8" rx="1"/></svg>+000 555 0147</div>
    <div class="contacts__row"><svg class="icon" viewBox="0 0 8 8"><rect x="0" y="3" width="8" height="5" rx="1"/><rect x="1" y="0" width="6" height="2" rx="1"/></svg>+000 555 0147</div>
    <div class="contacts__gap"></div>
    <div class="contacts__row"><svg class="icon" viewBox="0 0 8 8"><rect x="0" y="1" width="8" height="6" rx="1"/></svg>info@tarnwell.example</div>
    <div class="contacts__row"><svg class="icon" viewBox="0 0 8 8"><circle cx="4" cy="4" r="4"/></svg>www.tarnwell.example</div>
    <div class="contacts__addr contacts__addr--blue">24 Orchard Lane, Redvale<br>City Name, Country 9000 9000</div>
  </div>
</section>

<!-- Business card front, plain white -->
<section class="sheet" style="left:848px;top:258px;width:318px;height:196px">
  <div class="brand" style="left:58px;top:70px;font-size:22px"><span class="brand__dot" style="width:12px;height:12px"></span>Brelvo Company</div>
</section>

<!-- Letterhead -->
<section class="sheet" style="left:118px;top:480px;width:380px;height:492px">
  <div class="brand" style="left:32px;top:20px;font-size:12px;gap:4px"><span class="brand__dot" style="width:6px;height:6px"></span>Brelvo Company</div>
  <div class="divider" style="left:278px;top:16px;height:40px"></div>
  <div class="mini" style="left:283px;top:19px">
    +000 555 0147<br><span style="display:block;height:3px"></span>info@tarnwell.example<br>www.tarnwell.example<br><span style="display:block;height:3px"></span><span style="color:var(--text-blue)">24 Orchard Lane, Redvale<br>City Name, Country 9000 9000</span>
  </div>
  <svg class="band" viewBox="0 0 380 15" height="15" preserveAspectRatio="none"><polygon points="0,0 124,0 128,15 0,15" fill="var(--brand-blue)"/><polygon points="130,0 380,0 380,15 134,15" fill="var(--stone)"/></svg>
</section>

<!-- Envelope front -->
<section class="sheet" style="left:583px;top:510px;width:470px;height:206px">
  <div class="brand" style="left:17px;top:12px;font-size:10px;gap:4px"><span class="brand__dot" style="width:6px;height:6px"></span>Brelvo Company</div>
  <div class="mini" style="left:17px;top:49px">24 Orchard Lane, Redvale<br>City Name, Country 9000</div>
  <svg class="band" viewBox="0 0 470 16" height="16" preserveAspectRatio="none"><polygon points="0,0 151,0 155,16 0,16" fill="var(--brand-blue)"/><polygon points="158,0 470,0 470,16 162,16" fill="var(--stone)"/></svg>
</section>

<!-- Envelope back -->
<section class="sheet" style="left:585px;top:744px;width:469px;height:207px">
  <svg class="flap" viewBox="0 0 469 62" height="62"><path d="M0,0 H469 Q452,28 420,46 Q234,64 49,46 Q17,28 0,0 Z" fill="var(--brand-blue)"/></svg>
</section>

</body>
</html>
```